Project Title:
Dental Implant Overdenture Flyer (Retirement Village Target)
Objective:
Create a clean, trustworthy, and reassuring flyer aimed at older adults (60–85 years old) who struggle with loose dentures. The goal is to educate them about implant-retained “clip-on” dentures and encourage them to book a consultation.
Tone & Feel:
Warm, caring, non-intimidating
Premium but not “salesy”
Medical but easy to understand
Focus on improving quality of life (confidence, eating, comfort)
Target Audience:
Retirees / pensioners
Existing denture wearers
People frustrated with loose or uncomfortable dentures
Key Message:
“You don’t have to live with loose dentures anymore.”
Design Style:
Clean, minimal, modern
Soft colours (blues, greens, warm neutrals)
Easy-to-read large font
High contrast for older eyes
Avoid clutter
Imagery Suggestions:
Smiling older adults (natural, not stocky/overly staged)
Before/after lifestyle (eating, laughing, socialising)
Simple diagram showing denture clipping onto implants
Avoid graphic surgical images
Layout Suggestions:
A5 or DL flyer
Clear sections with headings
Icons for benefits
Strong call-to-action at bottom
HEADLINE (big and bold)
Tired of Loose Dentures?
Discover Secure “Clip-On” Teeth
🔹 PROBLEM SECTION
Do your dentures:
Slip or move when eating?
Make it hard to chew certain foods?
Feel uncomfortable or loose?
Affect your confidence when speaking or smiling?
You’re not alone — and there is a better solution.
🔹 SOLUTION SECTION
Implant-Retained “Clip-On” Dentures
We can secure your denture using just 2 dental implants, allowing your teeth to:
✔ Stay firmly in place
✔ Improve your ability to eat
✔ Feel more comfortable
✔ Boost your confidence
🔹 SIMPLE EXPLANATION (very important)
Small titanium implants are gently placed in the jaw.
Your denture then clips securely onto them, stopping movement.
🔹 PRICE SECTION (highlight this clearly)
$12,000
Includes:
2 dental implants
A brand new custom overdenture
Does not include sedation or extractions (if needed)
🔹 SEDATION
Sedation is available for comfort.
If you hold a pensioner card, you may receive a significant Vantrel rebate, often resulting in minimal out-of-pocket costs for sedation.
🔹 TRUST / REASSURANCE
Experienced implant clinician
Gentle, patient-focused care
Modern technology and techniques
🔹 CALL TO ACTION (VERY IMPORTANT)
Book a Free Consultation
📞 Call: 08 5127 3046
🌐 Visit: www.brolvenclinic.com.au
📍 Located near Tallowmere shopping centre
🔹 OPTIONAL TAGLINE
Eat Better. Feel Better. Smile with Confidence Again.
Please include some photos to illustrate what a clip on denture looks like with two implants.

```html
<!DOCTYPE html>
<html lang="en">
<head>
<meta charset="utf-8">
<title>Brolven Dental Clinic – Clip-On Dentures Flyer</title>
<link href="https://fonts.googleapis.com/css2?family=Roboto:wght@300;400;500;700;900&family=Roboto+Condensed:wght@400;700&display=swap" rel="stylesheet">
<style>
:root{
  --stage:#3e424d;
  --teal:#1a8ea4;
  --teal-dark:#127f96;
  --teal-light:#a9dbe4;
  --green:#5cc614;
  --text:#464a52;
  --white:#ffffff;
}
*{margin:0;padding:0;box-sizing:border-box}
html,body{width:1200px;height:1171px;overflow:hidden;background:var(--stage)}
body{font-family:'Roboto',sans-serif;position:relative}
.flyer{position:absolute;left:229px;top:58px;width:742px;height:1054px;background:var(--white);overflow:hidden;color:var(--text)}
.abs{position:absolute;white-space:nowrap}
.shapes{position:absolute;left:0;top:0;width:742px;height:1054px}
.portrait{position:absolute;left:0;top:0;width:270px;height:600px;
  background:linear-gradient(180deg,#e6f5f8 0%,#a9dbe4 35%,#cfd4d2 60%,rgba(26,142,164,0) 100%)}
/* brand */
.brand{left:340px;top:48px;text-align:center;width:330px}
.brand-mark{display:inline-block;width:18px;height:18px;border-radius:50%;background:var(--teal);vertical-align:middle;margin-right:10px}
.brand-name{font-size:28px;font-weight:500;letter-spacing:6px;color:var(--teal);vertical-align:middle}
.brand-sub{display:block;font-size:12px;font-weight:500;letter-spacing:5px;color:var(--teal);margin-top:8px}
/* headline */
.kicker{left:317px;top:147px;width:376px;text-align:center;font-size:28px;color:var(--green);font-weight:400}
.headline{left:310px;top:180px;width:390px;text-align:center;font-size:44px;line-height:49px;color:var(--teal);font-weight:400}
.headline b{font-weight:900}
.rule{position:absolute;height:1.5px;background:var(--green)}
/* problem list */
.problems{left:301px;top:302px;list-style:none;font-size:16px;line-height:25px}
.problems li::before{content:"";display:inline-block;width:6px;height:6px;border-radius:50%;background:var(--green);margin-right:11px;vertical-align:middle;position:relative;top:-2px}
.pill{position:absolute;left:306px;top:413px;width:397px;height:34px;border-radius:10px;background:var(--teal);color:var(--white);font-weight:700;font-size:17px;line-height:34px;text-align:center}
.section-title{left:301px;top:469px;width:403px;text-align:center;font-size:15px;font-weight:700;color:var(--teal)}
.section-title::before,.section-title::after{content:"";position:absolute;top:10px;width:35px;height:1.5px;background:var(--teal)}
.section-title::before{left:0}.section-title::after{right:0}
.intro{left:301px;top:495px;width:404px;text-align:center;font-size:16px;line-height:26px}
.benefits{left:318px;top:588px;list-style:none;font-size:16.5px;line-height:25.5px}
.benefits svg{width:19px;height:17px;vertical-align:-2px;margin-right:4px}
.vdivider{position:absolute;left:559px;top:560px;width:1px;height:158px;background:var(--green)}
.diagram{position:absolute;left:582px;top:560px;width:133px;height:162px;background:linear-gradient(180deg,#f3f5f6,#dfe3e5);border-radius:4px}
.explain{left:342px;top:732px;font-size:16.5px;line-height:25px}
.trust{left:368px;top:838px;list-style:none}
.trust li{display:flex;align-items:center;height:45px;font-size:19.5px;color:var(--text)}
.trust .icon{width:34px;height:34px;border-radius:50%;background:var(--green);margin-right:12px;display:flex;align-items:center;justify-content:center;flex:none}
/* left column */
.price-label{left:28px;top:535px;font-size:20px;color:var(--white)}
.price-box{position:absolute;left:31px;top:567px;width:208px;height:64px;border-radius:8px;background:var(--green);color:var(--white);font-weight:900;font-size:40px;text-align:center;line-height:64px}
.includes-label{left:19px;top:641px;font-size:15px;color:var(--white)}
.includes{left:19px;top:665px;list-style:none;font-family:'Roboto Condensed',sans-serif;font-weight:700;font-size:27px;line-height:32px;color:var(--white)}
.includes li{display:flex}
.includes li::before{content:"";width:9px;height:9px;border-radius:50%;background:var(--white);margin:12px 13px 0 3px;flex:none}
.fine{font-size:10px;color:var(--white);line-height:12px}
.sedation{left:20px;top:792px;font-family:'Roboto Condensed',sans-serif;color:var(--white);font-size:27px;line-height:31px}
.sedation b{font-weight:700;display:block}
.cta-tab{position:absolute;left:26px;top:941px;width:340px;height:42px;background:var(--white);border-top-left-radius:26px}
.cta{left:54px;top:948px;font-size:22px;font-weight:700;color:var(--teal)}
.footer{position:absolute;left:0;top:981px;width:715px;height:73px;background:var(--teal);color:var(--white)}
.footer .sep{position:absolute;top:15px;width:1px;height:42px;background:var(--white)}
.footer svg{position:absolute}
.phone{left:69px;top:23px;font-size:22px;font-weight:700}
.place{left:263px;top:15px;font-size:15.5px;line-height:21px}
.web{left:513px;top:26px;font-size:16px}
</style>
</head>
<body>
<main class="flyer">
  <div class="portrait" role="img" aria-label="Photo of a smiling older woman with white hair, hand on her chest"></div>
  <svg class="shapes" viewBox="0 0 742 1054" aria-hidden="true">
    <defs>
      <linearGradient id="panelFade" x1="0" y1="0" x2="0" y2="1">
        <stop offset="0" stop-color="#1a8ea4" stop-opacity="0"/>
        <stop offset="0.45" stop-color="#1a8ea4" stop-opacity="0"/>
        <stop offset="0.62" stop-color="#1a8ea4"/>
        <stop offset="1" stop-color="#1a8ea4"/>
      </linearGradient>
    </defs>
    <path d="M0 0 H274 C270 500 290 800 374 981 H0 Z" fill="url(#panelFade)"/>
  </svg>

  <div class="cta-tab"></div>
  <div class="abs cta">Book a Free Consultation</div>

  <svg class="shapes" viewBox="0 0 742 1054" aria-hidden="true">
    <path d="M274 0 C270 500 290 800 374 981" fill="none" stroke="#5cc614" stroke-width="5"/>
  </svg>

  <div class="abs brand"><span class="brand-mark"></span><span class="brand-name">BROLVEN</span><span class="brand-sub">DENTAL CLINIC</span></div>

  <div class="abs kicker">TIRED OF LOOSE DENTURES?</div>
  <h1 class="abs headline">DISCOVER SECURE<br><b>“CLIP-ON”</b> TEETH</h1>
  <div class="rule" style="left:320px;top:284px;width:369px"></div>

  <ul class="abs problems">
    <li>Slip or move when eating?</li>
    <li>Make it hard to chew certain foods?</li>
    <li>Feel uncomfortable or loose?</li>
    <li>Affect your confidence when speaking or smiling?</li>
  </ul>
  <div class="pill">You’re not alone — and there is a better solution.</div>

  <h2 class="abs section-title">IMPLANT-RETAINED “CLIP-ON” DENTURES</h2>
  <p class="abs intro">We can secure your denture using just 2 dental implants,<br>allowing your teeth to:</p>

  <ul class="abs benefits">
    <li><svg viewBox="0 0 19 17"><path d="M1 9 L7 15 L18 1" fill="none" stroke="#5cc614" stroke-width="3"/></svg>Stay firmly in place</li>
    <li><svg viewBox="0 0 19 17"><path d="M1 9 L7 15 L18 1" fill="none" stroke="#5cc614" stroke-width="3"/></svg>Improve your ability to eat</li>
    <li><svg viewBox="0 0 19 17"><path d="M1 9 L7 15 L18 1" fill="none" stroke="#5cc614" stroke-width="3"/></svg>Feel more comfortable</li>
    <li><svg viewBox="0 0 19 17"><path d="M1 9 L7 15 L18 1" fill="none" stroke="#5cc614" stroke-width="3"/></svg>Boost your confidence</li>
  </ul>
  <div class="vdivider"></div>
  <div class="diagram" role="img" aria-label="Diagram of a denture clipping onto dental implants placed in the jaw bone"></div>

  <p class="abs explain">Small titanium implants are gently placed in the jaw.<br>Your denture then clips securely onto them,<br>stopping movement.</p>
  <div class="rule" style="left:342px;top:820px;width:368px"></div>

  <ul class="abs trust">
    <li><span class="icon"><svg width="18" height="18" viewBox="0 0 18 18"><circle cx="9" cy="5" r="3.5" fill="none" stroke="#fff" stroke-width="1.6"/><path d="M2 17 C2 11 16 11 16 17" fill="none" stroke="#fff" stroke-width="1.6"/></svg></span>Experienced implant clinician</li>
    <li><span class="icon"><svg width="18" height="18" viewBox="0 0 18 18"><path d="M9 16 C1 10 1 4 5 3 C7 2.5 8.5 4 9 5 C9.5 4 11 2.5 13 3 C17 4 17 10 9 16Z" fill="none" stroke="#fff" stroke-width="1.6"/></svg></span>Gentle, patient-focused care</li>
    <li><span class="icon"><svg width="18" height="18" viewBox="0 0 18 18"><rect x="2" y="3" width="14" height="9" rx="1" fill="none" stroke="#fff" stroke-width="1.6"/><path d="M6 16 H12 M9 12 V16" stroke="#fff" stroke-width="1.6"/></svg></span>Modern technology and techniques</li>
  </ul>

  <div class="abs price-label">PRICE</div>
  <div class="price-box">$12,000</div>
  <div class="abs includes-label">Includes:</div>
  <ul class="abs includes">
    <li>2 dental implants</li>
    <li>A brand new custom<br>overdenture</li>
  </ul>
  <p class="abs fine" style="left:20px;top:766px">*Does not include sedation or extractions (if needed)</p>
  <div class="abs sedation"><b>SEDATION</b>Sedation is available for<br>comfort.</div>
  <p class="abs fine" style="left:20px;top:890px">* If you hold a pensioner card, you may receive a significant<br>Vantrel rebate, often resulting in minimal out-of-pocket<br>costs for sedation.</p>

  <footer class="footer">
    <svg style="left:39px;top:25px" width="24" height="24" viewBox="0 0 24 24" aria-hidden="true"><path d="M5 2 L9 6 L7 9 C8 12 11 15 14 16 L17 14 L21 18 L18 22 C10 21 3 14 2 5 Z" fill="#fff"/><path d="M14 2 A8 8 0 0 1 22 10 M14 6 A4 4 0 0 1 18 10" fill="none" stroke="#fff" stroke-width="1.6"/></svg>
    <div class="abs phone">08 5127 3046</div>
    <div class="sep" style="left:226px"></div>
    <svg style="left:238px;top:25px" width="16" height="22" viewBox="0 0 16 22" aria-hidden="true"><path d="M8 21 C3 14 1 11 1 8 A7 7 0 0 1 15 8 C15 11 13 14 8 21Z" fill="#fff"/><circle cx="8" cy="8" r="2.6" fill="#1a8ea4"/></svg>
    <div class="abs place">Located near<br>Tallowmere shopping centre</div>
    <div class="sep" style="left:474px"></div>
    <svg style="left:485px;top:28px" width="18" height="18" viewBox="0 0 18 18" aria-hidden="true"><circle cx="9" cy="9" r="7.5" fill="none" stroke="#fff" stroke-width="1.6"/><ellipse cx="9" cy="9" rx="3.2" ry="7.5" fill="none" stroke="#fff" stroke-width="1.4"/><path d="M1.5 9 H16.5" stroke="#fff" stroke-width="1.4"/></svg>
    <div class="abs web">www.brolvenclinic.com.au</div>
  </footer>
</main>
</body>
</html>
```